Tobin Quartz Portal Page . It's guarantee project!

We need a clean and professional modern web application portal page
That includes the Login & Application Selection screen

Also, I need to design both Desktop and Mobile sizes.
We have an example design for our target

The application is Jetty Schedule and related data.
Our client is a bit conservative.

Theme color preferred : #00508B (main) #DF0D83 (secondary)

Target Market(s)

Oil & Fuel & Gasoline

Number of Pages Required

2 page

Font styles to use
Sans Serif

Colors
0054AA
0677BA
7BADD7
CADEEF
E8F1F8
E54698
E96AAD
F1A4CE
F9D9EA
FCEFF6

Requirements
Must have
• Login Page & Main Screen

```html
<!DOCTYPE html>
<html lang="en">
<head>
<meta charset="utf-8">
<title>Tobin Quartz Portal</title>
<link href="https://fonts.googleapis.com/css2?family=Montserrat:wght@500;600;700;800&family=IBM+Plex+Sans:wght@400;500&display=swap" rel="stylesheet">
<style>
  :root{
    --brand-blue:#02528c;
    --brand-blue-mobile:#1b63a0;
    --brand-pink:#df0d83;
    --heading-blue:#0a4a82;
    --ink:#111418;
    --body-ink:#2b2f36;
    --band:#f2f6fa;
    --card-shadow:0 4px 14px rgba(20,40,70,.12);
    --circle:#dfe8f1;
    --page:#eef1f4;
    --field-text:#555b63;
    --art-soft:linear-gradient(135deg,#eaf2fa 0%,#cfe0ef 60%,#f5d9e8 100%);
  }
  *{box-sizing:border-box;margin:0;padding:0}
  html,body{width:1050px;height:1200px;overflow:hidden}
  body{background:var(--page);position:relative;font-family:"IBM Plex Sans",Arial,sans-serif;color:var(--body-ink)}
  .screen{position:absolute;overflow:hidden;background:#fff}

  /* ---------- Desktop login ---------- */
  .login-desktop{left:101px;top:62px;width:609px;height:340px}
  .login-desktop .panel{position:absolute;left:0;top:0;width:306px;height:100%;background:var(--brand-blue)}
  .brand-title{font-family:"Montserrat",Arial,sans-serif;font-weight:800;color:#fff;letter-spacing:.3px;text-transform:uppercase}
  .login-desktop .brand-title{position:absolute;left:13px;top:36px;font-size:18px}
  .signin-title{font-family:"Montserrat",Arial,sans-serif;font-weight:800;color:#fff;text-transform:uppercase}
  .login-desktop .signin-title{position:absolute;left:13px;top:114px;font-size:15px}
  .field{position:absolute;background:#fff;display:flex;align-items:center;justify-content:space-between;font-family:"Montserrat",Arial,sans-serif;font-weight:500;color:var(--field-text);text-transform:uppercase}
  .field svg{fill:#555}
  .login-desktop .field{left:13px;width:252px;height:28px;padding:0 10px 0 12px;font-size:8.5px}
  .login-desktop .field.email{top:149px}
  .login-desktop .field.password{top:189px}
  .btn-signin{position:absolute;background:var(--brand-pink);color:#fff;font-family:"Montserrat",Arial,sans-serif;font-weight:700;display:flex;align-items:center;justify-content:center;text-transform:uppercase}
  .login-desktop .btn-signin{left:13px;top:228px;width:252px;height:27px;font-size:9px}
  .login-desktop .art{position:absolute;left:332px;top:34px;width:270px;height:260px;background:var(--art-soft);border-radius:8px}
  .login-desktop .bottom-rule{position:absolute;left:306px;bottom:0;width:303px;height:2px;background:var(--brand-blue)}

  /* ---------- Mobile login ---------- */
  .login-mobile{left:776px;top:122px;width:208px;height:399px;background:var(--brand-blue-mobile)}
  .login-mobile .brand-title{position:absolute;left:0;width:100%;text-align:center;top:20px;font-size:15px}
  .login-mobile .signin-title{position:absolute;left:0;width:100%;text-align:center;top:55px;font-size:12px}
  .login-mobile .field{left:16px;width:180px;height:20px;padding:0 6px 0 9px;font-size:6px}
  .login-mobile .field.email{top:79px}
  .login-mobile .field.password{top:107px}
  .login-mobile .btn-signin{left:16px;top:135px;width:180px;height:20px;font-size:6.5px}
  .login-mobile .art-card{position:absolute;left:19px;top:176px;width:170px;height:140px;background:#fff;border-radius:8px;padding:10px}
  .login-mobile .art{width:100%;height:100%;background:var(--art-soft);border-radius:6px}

  /* ---------- Desktop main ---------- */
  .main-desktop{left:52px;top:601px;width:694px;height:537px}
  .topbar{position:absolute;display:flex;align-items:center}
  .topbar-title{position:absolute;font-family:"Montserrat",Arial,sans-serif;font-weight:800;color:var(--heading-blue);text-transform:uppercase;letter-spacing:.3px}
  .main-desktop .topbar-title{left:54px;top:12px;font-size:18px}
  .main-desktop .topbar{left:423px;top:15px;gap:12px;font-size:9.5px;color:var(--ink)}
  .user-item{display:flex;align-items:center;gap:4px}
  .toggle{width:20px;height:10px;border-radius:5px;background:#9aa0a6;position:relative}
  .toggle::after{content:"";position:absolute;left:1px;top:1px;width:8px;height:8px;border-radius:50%;background:#fff}
  .band{position:absolute;left:0;width:100%;background:var(--band)}
  .main-desktop .band{top:225px;height:124px}
  .deco-circle{position:absolute;border-radius:50%;background:var(--circle)}
  .art-card{position:absolute;background:#fff;border-radius:8px;box-shadow:var(--card-shadow);padding:12px 24px}
  .art-card .art{width:100%;height:100%;border-radius:6px}
  .art.planning{background:linear-gradient(135deg,#e8f1f8,#cadeef 55%,#f9d9ea)}
  .art.tracking{background:linear-gradient(135deg,#e8f1f8,#7badd7 70%,#f1a4ce)}
  .art.performance{background:linear-gradient(135deg,#e8f1f8,#cadeef 60%,#e96aad)}
  .section-title{position:absolute;font-family:"Montserrat",Arial,sans-serif;font-weight:700;color:var(--ink);text-transform:uppercase;font-size:13px;letter-spacing:.4px}
  .section-copy{position:absolute;font-size:10px;line-height:18px;color:var(--body-ink)}
  .section-copy p+p{margin-top:18px}

  /* ---------- Mobile main ---------- */
  .main-mobile{left:799px;top:669px;width:208px;height:399px}
  .main-mobile .topbar-title{left:11px;top:9px;font-size:10px}
  .main-mobile .topbar{right:10px;top:10px;gap:5px}
  .main-mobile .toggle{width:13px;height:6px}
  .main-mobile .toggle::after{width:4px;height:4px}
  .main-mobile .band{top:149px;height:113px}
  .main-mobile .art-card{left:47px;width:104px;height:70px;padding:8px 14px}
  .tile-label{position:absolute;left:0;width:100%;text-align:center;font-family:"Montserrat",Arial,sans-serif;font-weight:700;font-size:7.5px;color:var(--ink);text-transform:uppercase;letter-spacing:.3px}
</style>
</head>
<body>

<!-- Desktop sign in -->
<section class="screen login-desktop">
  <div class="panel">
    <h1 class="brand-title">Tobin Quartz</h1>
    <h2 class="signin-title">Sign In</h2>
    <div class="field email"><span>Email</span>
      <svg width="9" height="7" viewBox="0 0 9 7"><rect width="9" height="7" rx="1"/><path d="M0.5 0.8 4.5 3.8 8.5 0.8" stroke="#fff" stroke-width=".8" fill="none"/></svg>
    </div>
    <div class="field password"><span>Password</span>
      <svg width="10" height="8" viewBox="0 0 10 8"><path d="M0.5 4Q5 -1 9.5 4Q5 9 0.5 4Z"/><circle cx="5" cy="4" r="1.4" fill="#fff"/><path d="M1.5 7.5 8.5 .5" stroke="#fff" stroke-width="1.1"/><path d="M1.5 7.5 8.5 .5" stroke="#555" stroke-width=".6"/></svg>
    </div>
    <div class="btn-signin">Sign In</div>
  </div>
  <div class="art" role="img" aria-label="Illustration of a woman tapping a large phone login form with a padlock, gear and question bubble"></div>
  <div class="bottom-rule"></div>
</section>

<!-- Mobile sign in -->
<section class="screen login-mobile">
  <h1 class="brand-title">Tobin Quartz</h1>
  <h2 class="signin-title">Sign In</h2>
  <div class="field email"><span>Email</span>
    <svg width="6" height="5" viewBox="0 0 9 7"><rect width="9" height="7" rx="1"/><path d="M0.5 0.8 4.5 3.8 8.5 0.8" stroke="#fff" stroke-width=".8" fill="none"/></svg>
  </div>
  <div class="field password"><span>Password</span>
    <svg width="7" height="5" viewBox="0 0 10 8"><path d="M0.5 4Q5 -1 9.5 4Q5 9 0.5 4Z"/><circle cx="5" cy="4" r="1.4" fill="#fff"/></svg>
  </div>
  <div class="btn-signin">Sign In</div>
  <div class="art-card">
    <div class="art" role="img" aria-label="Illustration of a woman tapping a large phone login form with a padlock and gear"></div>
  </div>
</section>

<!-- Desktop application selection -->
<section class="screen main-desktop">
  <div class="topbar-title">Tobin Quartz</div>
  <div class="topbar">
    <span class="toggle"></span>
    <span class="user-item">
      <svg width="8" height="9" viewBox="0 0 8 9"><circle cx="4" cy="2.2" r="2.2" fill="#111"/><path d="M0 9Q0 4.6 4 4.6Q8 4.6 8 9Z" fill="#111"/></svg>
      Mara Vell
    </span>
    <span class="user-item">
      <svg width="9" height="7" viewBox="0 0 9 7"><rect width="9" height="7" rx="1" fill="#111"/><path d="M0.5 0.8 4.5 3.8 8.5 0.8" stroke="#fff" stroke-width=".8" fill="none"/></svg>
      mara.vell@example.com
    </span>
  </div>

  <div class="band"></div>

  <!-- Planning -->
  <div class="deco-circle" style="left:204px;top:156px;width:49px;height:49px"></div>
  <div class="art-card" style="left:53px;top:68px;width:181px;height:122px">
    <div class="art planning" role="img" aria-label="Illustration of a clock, a schedule calendar, a tanker ship and a woman ticking dates"></div>
  </div>
  <h3 class="section-title" style="left:273px;top:71px">Jetty Planning</h3>
  <div class="section-copy" style="left:273px;top:98px;width:360px">
    <p>Lorem ipsum dolor sit amet, consectetur adipiscing elit, sed do eiusmod tempor incididunt ut labore et dolore magna aliqua.</p>
    <p>Ut enim ad minim veniam, quis nostrud exercitation ullamco laboris nisi ut aliquip ex ea commodo consequat.</p>
  </div>

  <!-- Tracking -->
  <h3 class="section-title" style="left:54px;top:238px">Jetty Tracking</h3>
  <div class="section-copy" style="left:54px;top:261px;width:365px">
    <p>Lorem ipsum dolor sit amet, consectetur adipiscing elit, sed do eiusmod tempor incididunt ut labore et dolore magna aliqua.Ut enim ad minim veniam, quis nostrud exercitation ullamco laboris nisi ut aliquip ex ea commodo consequat.</p>
  </div>
  <div class="deco-circle" style="left:429px;top:314px;width:51px;height:51px"></div>
  <div class="art-card" style="left:459px;top:225px;width:181px;height:122px">
    <div class="art tracking" role="img" aria-label="Illustration of a hand holding a phone with a tracking screen, a ship, a clock and a location pin"></div>
  </div>

  <!-- Performance -->
  <div class="deco-circle" style="left:206px;top:468px;width:49px;height:49px"></div>
  <div class="art-card" style="left:53px;top:380px;width:181px;height:122px">
    <div class="art performance" role="img" aria-label="Illustration of a person working at a desk with a laptop and stacked reports"></div>
  </div>
  <h3 class="section-title" style="left:277px;top:383px">Jetty/Port Performance</h3>
  <div class="section-copy" style="left:277px;top:410px;width:360px">
    <p>Lorem ipsum dolor sit amet, consectetur adipiscing elit, sed do eiusmod tempor incididunt ut labore et dolore magna aliqua.</p>
    <p>Ut enim ad minim veniam, quis nostrud exercitation ullamco laboris nisi ut aliquip ex ea commodo consequat.</p>
  </div>
</section>

<!-- Mobile application selection -->
<section class="screen main-mobile">
  <div class="topbar-title">Tobin Quartz</div>
  <div class="topbar">
    <span class="toggle"></span>
    <svg width="5" height="6" viewBox="0 0 8 9"><circle cx="4" cy="2.2" r="2.2" fill="#111"/><path d="M0 9Q0 4.6 4 4.6Q8 4.6 8 9Z" fill="#111"/></svg>
    <svg width="6" height="5" viewBox="0 0 9 7"><rect width="9" height="7" rx="1" fill="#111"/><path d="M0.5 0.8 4.5 3.8 8.5 0.8" stroke="#fff" stroke-width=".8" fill="none"/></svg>
  </div>

  <div class="band"></div>

  <div class="deco-circle" style="left:133px;top:90px;width:28px;height:28px"></div>
  <div class="art-card" style="top:43px">
    <div class="art planning" role="img" aria-label="Illustration of a clock, a schedule calendar and a tanker ship"></div>
  </div>
  <div class="tile-label" style="top:128px">Jetty Planning</div>

  <div class="deco-circle" style="left:133px;top:211px;width:28px;height:28px"></div>
  <div class="art-card" style="top:164px">
    <div class="art tracking" role="img" aria-label="Illustration of a hand holding a tracking phone with a ship and pin"></div>
  </div>
  <div class="tile-label" style="top:249px">Jetty Tracking</div>

  <div class="deco-circle" style="left:133px;top:331px;width:28px;height:28px"></div>
  <div class="art-card" style="top:284px">
    <div class="art performance" role="img" aria-label="Illustration of a person working at a desk with a laptop"></div>
  </div>
  <div class="tile-label" style="top:369px">Jetty/Port Performance</div>
</section>

</body>
</html>
```